Forestry Mulching Business Cards

Business is called Timberline Clearing, We do forestry mulching which helps with wildfire mitigation, it helps reclaim your land. Just some ideas on what to say, get creative. I would like a Ravlex tracked skidsteer with a mulching head on it included somewhere, like the one i have attached in the photo. I would also like to add a groundhog popping out of the ground as a logo since i do not have one yet. Name and phone number and location should have a text slot, maybe include what brush removal/control does for you on the back in bulletins. I know i didnt make this very detailed but i want you guys to get creative!

```html
<!DOCTYPE html>
<html lang="en">
<head>
<meta charset="utf-8">
<title>Timberline Clearing – Business Cards</title>
<link rel="stylesheet" href="https://fonts.googleapis.com/css2?family=Rubik:wght@300;800;900&family=Saira+Condensed:wght@400;500;800&display=swap">
<style>
  :root {
    --page-bg: #d8ddc7;
    --forest-dark: #19310f;
    --forest-shade: #22401a;
    --leaf-green: #7b9f3b;
    --leaf-shade: #6f9234;
    --heading-dark: #1b4112;
    --text-light: #ffffff;
    --text-dark: #1b3410;
    --machine-light: #e4e7e1;
    --machine-mid: #9a9e9b;
    --machine-dark: #2c2f2d;
  }
  * { box-sizing: border-box; margin: 0; padding: 0; }
  html, body { width: 1200px; height: 1199px; overflow: hidden; }
  body { background: var(--page-bg); position: relative; }

  .card { position: absolute; width: 824px; overflow: hidden; }

  /* Front */
  .card-front { left: 186px; top: 76px; height: 471px; background: var(--forest-dark); }
  .card-front .treeline {
    position: absolute; left: 0; right: 0; bottom: 17px; height: 290px;
    background: linear-gradient(to bottom, rgba(34,64,26,0) 0%, rgba(34,64,26,0.75) 55%, rgba(34,64,26,0.4) 100%);
  }
  .card-front .accent-band { position: absolute; left: 0; right: 0; bottom: 0; height: 17px; background: var(--leaf-green); }

  .brand-mark {
    position: absolute; left: 168px; top: 91px; width: 74px; height: 74px;
    border-radius: 50%; background: var(--leaf-green);
  }
  .brand-name {
    position: absolute; left: 0; width: 410px; top: 168px; text-align: center;
    font-family: "Saira Condensed", sans-serif; font-weight: 800;
    font-size: 64px; line-height: 54px; color: var(--leaf-green); text-transform: uppercase;
  }
  .divider { position: absolute; left: 410px; top: 68px; width: 1px; height: 229px; background: var(--leaf-green); }

  .contact-list { position: absolute; left: 466px; top: 0; list-style: none; }
  .contact-item {
    position: absolute; left: 0; display: flex; align-items: center; white-space: nowrap;
    font-family: "Saira Condensed", sans-serif; font-weight: 500; color: var(--text-light);
  }
  .contact-item svg { width: 18px; height: 18px; fill: var(--leaf-green); margin-right: 14px; flex: none; }
  .contact-name { top: 99px; font-size: 30px; }
  .contact-address { top: 158px; font-size: 23px; }
  .contact-phone { top: 195px; font-size: 23px; }
  .contact-email { top: 231px; font-size: 23px; }

  .tagline {
    position: absolute; left: 0; right: 0; top: 380px; text-align: center;
    font-family: "Rubik", sans-serif; font-weight: 300; font-size: 33px; color: var(--text-light);
  }

  /* Back */
  .card-back { left: 181px; top: 638px; height: 477px; background: var(--leaf-green); }
  .card-back .treeline {
    position: absolute; left: 0; right: 0; bottom: 17px; height: 330px;
    background: linear-gradient(to bottom, rgba(111,146,52,0) 0%, rgba(111,146,52,0.85) 60%, rgba(111,146,52,0.5) 100%);
  }
  .card-back .accent-band { position: absolute; left: 0; right: 0; bottom: 0; height: 17px; background: var(--forest-dark); }

  .benefits-heading {
    position: absolute; left: 50px; top: 38px;
    font-family: "Rubik", sans-serif; font-weight: 900; font-size: 37px; line-height: 48px;
    color: var(--heading-dark); text-transform: uppercase;
  }
  .benefits-list { position: absolute; left: 50px; top: 158px; list-style: none; }
  .benefit {
    display: flex; align-items: center; height: 39px;
    font-family: "Saira Condensed", sans-serif; font-weight: 400; font-size: 29.5px; color: var(--text-dark);
  }
  .benefit svg { width: 24px; height: 20px; margin-right: 22px; flex: none; }

  .machine-photo {
    position: absolute; left: 402px; top: 166px; width: 370px; height: 264px; border-radius: 28px;
    background: linear-gradient(140deg, var(--machine-dark) 0%, var(--machine-mid) 30%, var(--machine-light) 55%, var(--machine-mid) 75%, var(--machine-dark) 100%);
    box-shadow: 0 10px 24px rgba(27, 52, 16, 0.35);
  }
</style>
</head>
<body>

<section class="card card-front">
  <div class="treeline" role="img" aria-label="Faint silhouette of a conifer treeline"></div>

  <div class="brand-mark" aria-hidden="true"></div>
  <h1 class="brand-name">Timberline<br>Clearing</h1>

  <div class="divider"></div>

  <ul class="contact-list">
    <li class="contact-item contact-name">
      <svg viewBox="0 0 24 24"><circle cx="12" cy="7" r="5"/><path d="M2 23c0-6 4.5-9 10-9s10 3 10 9z"/></svg>Name
    </li>
    <li class="contact-item contact-address">
      <svg viewBox="0 0 24 24"><path d="M12 1C7.6 1 4 4.5 4 9c0 6 8 14 8 14s8-8 8-14c0-4.5-3.6-8-8-8zm0 11a3 3 0 1 1 0-6 3 3 0 0 1 0 6z"/></svg>Address line here
    </li>
    <li class="contact-item contact-phone">
      <svg viewBox="0 0 24 24"><path d="M6.6 10.8a15 15 0 0 0 6.6 6.6l2.2-2.2c.3-.3.7-.4 1-.2 1.1.4 2.3.6 3.6.6.6 0 1 .4 1 1V20c0 .6-.4 1-1 1A17 17 0 0 1 3 4c0-.6.4-1 1-1h3.5c.6 0 1 .4 1 1 0 1.3.2 2.5.6 3.6.1.3 0 .7-.2 1z"/></svg>000 111 2222
    </li>
    <li class="contact-item contact-email">
      <svg viewBox="0 0 24 24"><path d="M2 5h20v14H2z"/><path d="M3 6l9 7 9-7" fill="none" stroke="#19310f" stroke-width="2"/></svg>name@emailaddress.com
    </li>
  </ul>

  <p class="tagline">FORESTRY MULCHING AND BRUSH CONTROL</p>
  <div class="accent-band"></div>
</section>

<section class="card card-back">
  <div class="treeline" role="img" aria-label="Faint silhouette of a conifer treeline"></div>

  <h2 class="benefits-heading">What brush removal / control<br>can do for you</h2>

  <ul class="benefits-list">
    <li class="benefit"><svg viewBox="0 0 24 20"><path d="M2 10l7 7L22 3" fill="none" stroke="#fff" stroke-width="5"/></svg>Wildfire mitigation</li>
    <li class="benefit"><svg viewBox="0 0 24 20"><path d="M2 10l7 7L22 3" fill="none" stroke="#fff" stroke-width="5"/></svg>Environmentally friendly</li>
    <li class="benefit"><svg viewBox="0 0 24 20"><path d="M2 10l7 7L22 3" fill="none" stroke="#fff" stroke-width="5"/></svg>Prevents soil erosion</li>
    <li class="benefit"><svg viewBox="0 0 24 20"><path d="M2 10l7 7L22 3" fill="none" stroke="#fff" stroke-width="5"/></svg>Improves soil quality</li>
    <li class="benefit"><svg viewBox="0 0 24 20"><path d="M2 10l7 7L22 3" fill="none" stroke="#fff" stroke-width="5"/></svg>Weed and pest control</li>
    <li class="benefit"><svg viewBox="0 0 24 20"><path d="M2 10l7 7L22 3" fill="none" stroke="#fff" stroke-width="5"/></svg>Fast and efficient</li>
    <li class="benefit"><svg viewBox="0 0 24 20"><path d="M2 10l7 7L22 3" fill="none" stroke="#fff" stroke-width="5"/></svg>Cost effective</li>
  </ul>

  <div class="machine-photo" role="img" aria-label="Photo of a white Ravlex tracked skid steer fitted with a black forestry mulching head"></div>
  <div class="accent-band"></div>
</section>

</body>
</html>
```